Truck and Van wrap design

We need designs for our trucks and vans. Our Logo and contact details including phone number (+97148517300), email (hello@zelvoraproduce.com), and website have to be incorporated into the design. Our company colors are white, green, red, and yellow in the same shades used in the logo. This design needs to be in .ai (Adobe Illustrator) format. We have 5 different size vehicles that need designs. We would prefer a scalable design that we can resize for future use.Truck 1 DimentionsHeight: 2.1 MetersWidth: 2.1 MetersLength: 5 MetersTruck 2 DimensionsHeight: 2.1 MetersWidth: 2.1 MetersLength: 4.3 MetersTruck 3 DimensionsHeight: 2.75 MetersWidth: 2.6 MetersLength: 7 MetersTrailer DimensionsHeight: 2.5 MetersWidth: 2.6 MetersLength: 13.58 MetersVan DimensionsHeight: 1.7 Meters Width: 1.7 MetersLength: 3.5 MetersYou can find pictures of the vehicles and our logo attached for reference. The trucks and trailer only need the two sides and back end designed while the van is a full wrap.
Please try to keep the designs clean and avoid the use of too many photos.

```html
<!DOCTYPE html>
<html lang="en">
<head>
<meta charset="UTF-8">
<title>Zelvora Produce – Vehicle Wrap</title>
<link href="https://fonts.googleapis.com/css2?family=Oswald:wght@400;500&display=swap" rel="stylesheet">
<style>
  :root {
    --brand-red: #a51c10;
    --brand-green: #7dc242;
    --brand-yellow: #f5b51c;
    --ink: #3a3a3a;
    --panel-edge: #d6d6d6;
    --white: #ffffff;
  }
  * { margin: 0; padding: 0; box-sizing: border-box; }
  html, body { width: 1200px; height: 1200px; overflow: hidden; background: var(--white); }
  body { position: relative; font-family: "Oswald", "Arial Narrow", sans-serif; }

  .wrap-side, .wrap-rear {
    position: absolute;
    background: var(--white);
    border: 1px solid var(--panel-edge);
    overflow: hidden;
  }
  .wrap-side { left: 98px; top: 426px; width: 1072px; height: 302px; }
  .wrap-rear { left: 506px; top: 876px; width: 322px; height: 304px; }

  .contact-band {
    position: absolute;
    left: 0; right: 0;
    background: var(--brand-red);
    color: var(--white);
  }
  .wrap-side .contact-band {
    top: 59px; height: 57px;
    display: flex; align-items: center; justify-content: space-between;
    padding: 0 12px 0 303px;
  }
  .band-web, .band-mail { font-size: 24px; font-weight: 400; letter-spacing: 0.2px; }
  .band-phone { font-size: 46px; font-weight: 500; line-height: 1; }
  .wrap-rear .contact-band { top: 40px; height: 58px; }

  .produce-photo {
    position: absolute;
    left: 0; right: 0; top: 116px; bottom: 0;
    background: linear-gradient(90deg, #f0a23a 0%, #c7d94a 22%, #b7d36a 40%, #3a3540 58%, #d8a43a 72%, #e6b93a 85%, #c9692b 100%);
  }
  .basket-photo {
    position: absolute;
    left: 166px; top: 24px; width: 148px; height: 164px;
    border-radius: 10px;
    background: radial-gradient(circle at 50% 60%, #d2b07a 0%, #b9d36a 55%, #f2d04a 100%);
  }

  .brand-disc {
    position: absolute;
    border-radius: 50%;
    background: var(--white);
    border: 11px solid var(--brand-green);
    display: flex; flex-direction: column; align-items: center; justify-content: center;
  }
  .wrap-side .brand-disc { left: 8px; top: 0; width: 284px; height: 284px; }
  .wrap-rear .brand-disc { left: 14px; top: 32px; width: 160px; height: 160px; border-width: 8px; }

  .brand-name { color: var(--ink); font-weight: 400; letter-spacing: 3px; line-height: 1; }
  .wrap-side .brand-name { font-size: 44px; margin-top: 40px; }
  .wrap-rear .brand-name { font-size: 25px; letter-spacing: 2px; }
  .brand-since { color: var(--brand-red); font-size: 28px; font-weight: 400; margin-top: 36px; line-height: 1; }

  .rear-contacts {
    position: absolute; left: 0; right: 0; top: 196px;
    text-align: center; color: var(--brand-red); line-height: 1;
  }
  .rear-phone { font-size: 32px; font-weight: 400; margin-left: 14px; }
  .rear-web { font-size: 25px; margin-top: 8px; margin-left: 14px; }
  .rear-mail { font-size: 25px; margin-top: 7px; }
</style>
</head>
<body>
  <section class="wrap-side" aria-label="Trailer side panel">
    <div class="produce-photo" role="img" aria-label="Row of fresh fruit: kiwi, oranges, lemons, limes, green and black grapes, ginger, apples, bananas, pears and mango"></div>
    <div class="contact-band">
      <span class="band-web">zelvoraproduce.com</span>
      <span class="band-phone">+9 714 851 7300</span>
      <span class="band-mail">hello@zelvoraproduce.com</span>
    </div>
    <div class="brand-disc">
      <span class="brand-name">ZELVORA</span>
      <span class="brand-since">SINCE 1985</span>
    </div>
  </section>

  <section class="wrap-rear" aria-label="Trailer rear panel">
    <div class="contact-band"></div>
    <div class="basket-photo" role="img" aria-label="Woven basket filled with grapes, pineapple, bananas, apples and pears"></div>
    <div class="brand-disc">
      <span class="brand-name">ZELVORA</span>
    </div>
    <div class="rear-contacts">
      <div class="rear-phone">+9 714 851 7300</div>
      <div class="rear-web">zelvoraproduce.com</div>
      <div class="rear-mail">hello@zelvoraproduce.com</div>
    </div>
  </section>
</body>
</html>
```